Business Card Design - Construction Company

Torvane Construction is in need of a sharp, modern business card design that has an architectural/high fashion feel.

We are looking for a two sided card.

One side simple dark grey/black with some texture in the background. e.g. (a mosaic of simple interconnecting shapes or a shadow of the logo.) Something to draw attention and create interest.It will need to feature a large Torvane construction logo (files attached) in metallic gradient or plain white.

The other side should contain all of our information:

(in largest text)
Name of person
Torvane Construction Pty. Ltd.

Licensed builders specialising in:
- Bathrooms
- Kitchens
- Commercial interiors

(mid sized text)
Phone number
Fax number
person@torvaneconstruction.example.au
www. torvaneconstruction.example.au

(smaller text)
ABN: 47209836512
BSA license: xxx-xxxx
PO Box 8640 Dunmore QLD 4170 (address)

Target Market(s)

professional home and business owners

Industry/Entity Type

Construction

Requirements
Must have
• Must be bold, professional looking and modern.
Nice to have
• We are undecided as to what kind of printing we will go with.
Definitely square edged.
Probably high quality satin card.
We are also interested in designs that would work well on transparent or translucent plastic.
Ideally we would print two versions.
Should not have
• Nothing with an antique feel.
No wild colours. Small amounts of colour can be good in the right place.

```html
<!DOCTYPE html>
<html lang="en">
<head>
<meta charset="utf-8">
<title>Torvane Construction – Business Cards</title>
<link rel="stylesheet" href="https://fonts.googleapis.com/css2?family=Michroma&family=Arimo:ital,wght@0,400;1,400&family=Tinos&display=swap">
<style>
  :root {
    --page-bg: #e4e4e4;
    --card-bg: #1f1c1b;
    --card-bg-edge: #2a2625;
    --silver-light: #f2f2f2;
    --silver-mid: #b8b8b8;
    --silver-dark: #6e6e6e;
    --text-main: #f1f1f1;
    --text-soft: #d6d6d6;
    --brand: #d9d9d9;
  }
  * { box-sizing: border-box; margin: 0; padding: 0; }
  html, body { width: 1200px; height: 951px; overflow: hidden; }
  body {
    background: var(--page-bg);
    position: relative;
    font-family: "Arimo", Arial, sans-serif;
  }
  .card {
    position: absolute;
    width: 620px;
    height: 372px;
    background: radial-gradient(ellipse at 40% 40%, var(--card-bg-edge), var(--card-bg) 70%);
    overflow: hidden;
  }
  .card--front { left: 110px; top: 70px; }
  .card--back  { left: 470px; top: 505px; }

  .silver-bar {
    position: absolute;
    background: linear-gradient(90deg, var(--silver-dark), var(--silver-light) 40%, var(--silver-mid) 70%, var(--silver-dark));
    border-radius: 3px;
  }
  .card--front .silver-bar { top: 0; bottom: 0; width: 30px; }
  .card--front .silver-bar--left { left: 0; }
  .card--front .silver-bar--right { right: 0; }
  .card--back .silver-bar { top: 14px; bottom: 14px; width: 18px; }
  .card--back .silver-bar--left { left: 14px; }
  .card--back .silver-bar--right { right: 14px; }

  .brand {
    position: absolute;
    color: var(--brand);
    font-family: "Michroma", sans-serif;
    font-weight: 400;
    text-align: center;
    line-height: 1;
  }
  .brand__name { display: block; }
  .brand__sub { display: block; letter-spacing: 0.3em; }
  .card--front .brand { left: 0; right: 0; top: 150px; }
  .card--front .brand__name { font-size: 58px; letter-spacing: 0.04em; }
  .card--front .brand__sub { font-size: 17px; margin-top: 14px; }
  .card--back .brand { left: 52px; width: 230px; top: 108px; }
  .card--back .brand__name { font-size: 34px; }
  .card--back .brand__sub { font-size: 11px; margin-top: 9px; }

  .contact {
    position: absolute;
    left: 298px;
    top: 44px;
    color: var(--text-main);
  }
  .contact__name { font-size: 22px; letter-spacing: 0.02em; text-transform: uppercase; }
  .contact__role { font-size: 15px; font-style: italic; color: var(--text-soft); margin-top: 2px; }
  .contact__lines { list-style: none; margin-top: 18px; font-size: 13px; line-height: 19px; }
  .contact__lines li { display: flex; align-items: center; gap: 7px; }
  .contact__lines svg { width: 12px; height: 12px; flex: none; }
  .contact__legal { margin-top: 14px; font-size: 11.5px; line-height: 16px; color: var(--text-soft); }

  .tagline {
    position: absolute;
    left: 48px; right: 48px;
    top: 282px;
    text-align: center;
    font-family: "Tinos", "Times New Roman", serif;
    font-size: 17px;
    line-height: 24px;
    letter-spacing: 0.1em;
    color: var(--text-soft);
    text-transform: uppercase;
  }
</style>
</head>
<body>

  <section class="card card--front" aria-label="Card front">
    <div class="silver-bar silver-bar--left"></div>
    <div class="silver-bar silver-bar--right"></div>
    <div class="brand">
      <span class="brand__name">TORVANE</span>
      <span class="brand__sub">CONSTRUCTION</span>
    </div>
  </section>

  <section class="card card--back" aria-label="Card back">
    <div class="silver-bar silver-bar--left"></div>
    <div class="silver-bar silver-bar--right"></div>
    <div class="brand">
      <span class="brand__name">TORVANE</span>
      <span class="brand__sub">CONSTRUCTION</span>
    </div>

    <div class="contact">
      <p class="contact__name">Marcus Delaney</p>
      <p class="contact__role">manager</p>
      <ul class="contact__lines">
        <li>
          <svg viewBox="0 0 12 12" aria-hidden="true"><circle cx="6" cy="6" r="5.5" fill="none" stroke="#eee"/><path d="M4 3.2c.5-.3.9 0 1 .5l.2.8-.6.5c.3.8.9 1.4 1.6 1.7l.5-.6.8.2c.5.1.8.5.5 1-.5.8-1.6.8-2.6.1C4.3 6.6 3.6 5.6 3.6 4.6c0-.6.1-1.1.4-1.4z" fill="#eee"/></svg>
          070 512 8836
        </li>
        <li>
          <svg viewBox="0 0 12 12" aria-hidden="true"><rect x="1" y="5" width="10" height="6" rx="1" fill="#eee"/><rect x="3" y="1" width="6" height="4" fill="none" stroke="#eee"/></svg>
          84 917 2250
        </li>
        <li>
          <svg viewBox="0 0 12 12" aria-hidden="true"><rect x="0.5" y="2.5" width="11" height="7" fill="none" stroke="#eee"/><path d="M0.5 2.5 6 7l5.5-4.5" fill="none" stroke="#eee"/></svg>
          marcus@torvaneconstruction.example.au
        </li>
        <li>
          <svg viewBox="0 0 12 12" aria-hidden="true"><rect x="0.5" y="0.5" width="11" height="11" rx="1.5" fill="#eee"/><circle cx="6" cy="6" r="3.5" fill="none" stroke="#222"/><path d="M2.5 6h7M6 2.5v7" stroke="#222"/></svg>
          www. torvaneconstruction.example.au
        </li>
      </ul>
      <div class="contact__legal">
        <p>ABN: 47209836512</p>
        <p>BSA license: xxx-xxxx</p>
        <p>PO Box 8640 Dunmore QLD 4170</p>
      </div>
    </div>

    <p class="tagline">Licensed builders specialising in<br>bathrooms kitchens, commercial fitouts</p>
  </section>

</body>
</html>
```